Cannabis Processor Vape Cart Box Design/Concentrate Jar Box Design

We are a solventless (no chemicals added) cannabis processor in the state of Michigan. We have 2 products, one is a vape cartridge and one is a 5mL clear glass concentrate jar with a black lid. We need designs that correlates with our logo for their box packaging. Each piece of packaging has an opening so you can see the jar/vape cartridge and their contents. Each piece of packaging needs to have the universal symbol of cannabis, which is on the bottom right hand corner of the vape cartridge container for reference. Also on the jar box top lid we need the net weight listed like this (NET WT. 1.0g / 0.0176oz) I have attached some examples of the packaging boxes, the jar we will be using, and our logo so you know what you are shooting for. On the Jar Box there will be a hole in the center of the bottom of the box, so people can see the jar and it's contents. On the back of the jar box I would like the following (Here at 842 Resins, our mission is to be make the purest concentrates available. We strive to fully represent the true essence of the flower through our solventless processes. At 842 Resins we only use the finest Michigan grown, pesticide-free flowers for extraction. We pride ourselves on our chemical-free extraction methods, and are constantly innovating to bring better and cleaner concentrates for Medicinal and Recreational use.) On the Vape Cartridge box there will be a straight up and down hole in the shape of the vape cartridge instead of the Michigan shape. Get creative, but remember that you can not use any cannabis leaf symbol on the design. On the top of the back of the vape cartridge box I want the following (Here at 842 Resins, our mission is to be make the purest vape cartridge available. We strive to fully represent the true essence of the flower through our solventless processes. At 842 Resins we only use the finest Michigan grown, pesticide-free flowers for extraction. We pride ourselves on our chemical-free extraction methods, and are constantly innovating to bring better and cleaner products for both Medicinal and Recreational use.) We look forward to your submissions, and to the best design we thank you in advance. I almost forgot, we would prefer a black base with white lettering, but we are open to any creative ideas, so please submit more options than what we requested, because the best look will win.

```html
<!DOCTYPE html>
<html lang="en">
<head>
<meta charset="utf-8">
<title>842 Resins – Concentrate Jar Box Dieline</title>
<link rel="stylesheet" href="https://fonts.googleapis.com/css2?family=Cabin:wght@400;500&family=Roboto+Condensed:wght@700&display=swap">
<style>
  :root {
    --bg: #161616;
    --panel: #262626;
    --panel-edge: #1c1c1c;
    --ink: #f4f4f4;
    --gold-pale: #f3e2a6;
    --gold: #a88a05;
    --gold-deep: #4a3010;
    --window-a: #f7c63a;
    --window-b: #ffd98a;
    --window-c: #f7a21b;
  }
  * { margin: 0; padding: 0; box-sizing: border-box; }
  html, body { width: 1077px; height: 1200px; overflow: hidden; background: var(--bg); }
  .canvas { position: relative; width: 1077px; height: 1200px; background: var(--bg); font-family: "Cabin", sans-serif; color: var(--ink); }

  .panel {
    position: absolute; width: 237px; height: 236px;
    background: linear-gradient(90deg, var(--panel-edge) 0%, var(--panel) 12%, var(--panel) 88%, var(--panel-edge) 100%);
  }
  .panel--lid    { left: 573px; top: 447px; }
  .panel--back   { left: 99px;  top: 682px; }
  .panel--left   { left: 336px; top: 682px; }
  .panel--front  { left: 572px; top: 682px; }
  .panel--right  { left: 809px; top: 682px; }
  .panel--bottom { left: 573px; top: 918px; background: linear-gradient(180deg, #1d1d1d 0%, var(--panel) 20%, var(--panel) 100%); }

  .gold-band {
    position: absolute; left: 610px; top: 450px; width: 160px; height: 296px;
    background: linear-gradient(180deg, var(--gold-pale) 0%, #d9bf5a 25%, var(--gold) 50%, #7a5d0a 75%, var(--gold-deep) 100%);
    z-index: 2;
  }
  .net-weight {
    position: absolute; top: 108px; width: 100%; text-align: center;
    font-size: 11.5px; color: var(--ink); letter-spacing: 0.1px;
  }
  .brand {
    position: absolute; width: 100%; text-align: center;
    font-family: "Cabin", sans-serif; font-weight: 400; color: var(--ink);
    letter-spacing: 3px; white-space: nowrap;
  }
  .gold-band .brand { top: 258px; font-size: 17px; }
  .panel--left .brand, .panel--right .brand { top: 100px; font-size: 17px; }
  .panel--back .brand { top: 207px; font-size: 10.5px; letter-spacing: 2px; }

  .mission {
    position: absolute; left: 22px; right: 22px; top: 26px;
    font-size: 8.6px; line-height: 12.6px; text-align: center;
  }
  .mission p + p { margin-top: 12px; }

  .product-name {
    position: absolute; top: 109px; width: 100%; text-align: center;
    font-family: "Roboto Condensed", sans-serif; font-weight: 700;
    font-size: 13px; line-height: 17px; letter-spacing: 0.3px;
  }
  .thc-symbol { position: absolute; left: 429px; top: 147px; }
  .panel--front .thc-symbol { left: 213px; top: 144px; }

  .window {
    position: absolute; top: 188px; left: 24px; width: 183px; height: 32px;
    border-radius: 11px;
    background: linear-gradient(90deg, var(--window-a) 0%, var(--window-b) 55%, var(--window-c) 100%);
    box-shadow: inset 0 3px 6px rgba(120,70,0,0.45);
  }
  .panel--front .window { left: 25px; }
  .panel--right .window { left: 28px; }
</style>
</head>
<body>
<div class="canvas">
  <div class="panel panel--lid"></div>

  <div class="gold-band">
    <div class="net-weight">NET WT. 1.0G / 0.0176OZ</div>
    <div class="brand">842 RESINS</div>
  </div>

  <div class="panel panel--back">
    <div class="mission">
      <p>Here at 842 Resins, our mission is to be make the purest concentrates available. We strive to fully represent the true essence of the flower through our solventless processes.</p>
      <p>At 842 Resins we only use the finest Michigan grown, pesticide-free flowers for extraction. We pride ourselves on our chemical-free extraction methods, and are constantly innovating to bring better and cleaner concentrates for Medicinal and Recreational use.</p>
    </div>
    <div class="brand">842 RESINS</div>
  </div>

  <div class="panel panel--left">
    <div class="brand">842 RESINS</div>
    <div class="window" role="img" aria-label="Window showing the concentrate jar"></div>
  </div>

  <div class="panel panel--front">
    <div class="product-name">PREMIUM CANNABIS<br>CONCENTRATE</div>
    <svg class="thc-symbol" width="32" height="32" viewBox="0 0 32 32" aria-label="THC warning symbol">
      <path d="M16 1.5 L30.5 16 L16 30.5 L1.5 16 Z" fill="none" stroke="#f4f4f4" stroke-width="1.6"/>
      <rect x="15.2" y="6.5" width="1.6" height="6" fill="#f4f4f4"/>
      <rect x="15.2" y="13.6" width="1.6" height="1.6" fill="#f4f4f4"/>
      <text x="16" y="21.5" text-anchor="middle" font-family="Roboto Condensed, sans-serif" font-weight="700" font-size="6.5" fill="#f4f4f4">THC</text>
    </svg>
    <div class="window" role="img" aria-label="Window showing the concentrate jar"></div>
  </div>

  <div class="panel panel--right">
    <div class="brand">842 RESINS</div>
    <div class="window" role="img" aria-label="Window showing the concentrate jar"></div>
  </div>

  <div class="panel panel--bottom"></div>
</div>
</body>
</html>
```